218 MARLOWE AVE NORTH FEATURES AND FINISHES

In need of a flyer that lists the features, floor plans and renderings of homes that we are constructing for sale. Could you please ensure that the word document is used in a creative way

See below for information to add:

www.halvorbuildgroup.ca
www.halvorresidencesdunmore.com
For inquiries and pricing, please contact 905 314 6782.

Target Market(s)

interested home buyers

Industry/Entity Type

Home Builder

Font styles to use
Sans Serif

Requirements
Must have
• must be creative
must have floor plans
must have features looking stylish
must have halvor logos

Nice to have
• creative selling features

IF YOU CAN FIND A WAY TO USE THE FLOOR PLANS THAT ARE IN THE ATTACHED CONSTRUCTION DRAWINGS....THAT WOULD BE GREAT. LOOKING TO HAVE THE MAIN FLOOR AND 2ND FLOOR LAYOUT ON THERE. IF YOU CAN MAKE LESS CLUTTER BY REMOVING SOME DIMENSIONS THAT WOULD BE AWESOME
Should not have
• please make it professional looking

```html
<!DOCTYPE html>
<html lang="en">
<head>
<meta charset="utf-8">
<title>218 Marlowe Ave North – Features and Finishes</title>
<link href="https://fonts.googleapis.com/css2?family=Exo+2:wght@300;400&family=Michroma&family=Open+Sans:wght@400;600&family=Roboto:wght@400;700&display=swap" rel="stylesheet">
<style>
  :root{
    --backdrop:#4d4d4d;
    --ink:#231f20;
    --gold:#c9a070;
    --tan:#c6a27a;
    --peach:#fbe3cf;
    --white:#ffffff;
    --text:#2b2626;
    --sky:#b9d3e6;
    --lawn:#4f7a3a;
    --paper:#ffffff;
    --line:#c9a98a;
  }
  *{box-sizing:border-box;margin:0;padding:0}
  html,body{width:1200px;height:809px;overflow:hidden}
  body{background:var(--backdrop);position:relative;font-family:"Open Sans",sans-serif}
  .sheet{position:absolute;top:89px;width:489px;height:632px;background:var(--ink);overflow:hidden}
  .sheet--front{left:73px}
  .sheet--back{left:627px}

  .hero-render{position:absolute;left:0;top:0;width:489px;height:279px;
    background:linear-gradient(180deg,var(--sky) 0%,#dfe6ea 45%,#c9cfcf 70%,var(--lawn) 100%)}
  .headline-band{position:absolute;left:0;top:279px;width:489px;height:51px;display:flex;align-items:center;justify-content:center;
    font-family:"Roboto",sans-serif;font-weight:400;font-size:30px;color:var(--white);letter-spacing:-0.6px;white-space:nowrap}
  .headline-band strong{color:var(--gold);font-weight:700;margin-left:8px}
  .plan-area{position:absolute;left:0;top:330px;width:489px;height:182px;background:var(--paper)}
  .plan-section{position:absolute;left:32px;top:14px;width:272px;height:148px;background:linear-gradient(180deg,#f2f2f2,#d8d8d8)}
  .plan-roof{position:absolute;left:324px;top:10px;width:140px;height:160px;background:linear-gradient(180deg,#efefef,#d4d4d4)}

  .features-head{position:absolute;left:0;top:0;width:489px;height:48px;display:flex;align-items:center;justify-content:center;
    font-family:"Exo 2",sans-serif;font-weight:400;font-size:24px;letter-spacing:1.4px;color:var(--white);white-space:nowrap}
  .features-head span{color:var(--gold);margin-right:8px}
  .features-body{position:absolute;left:0;top:48px;width:489px;height:465px;background:var(--peach)}
  .feature-list{position:absolute;top:15px;list-style:none;font-size:10px;line-height:13px;color:var(--text);
    display:flex;flex-direction:column}
  .feature-list--left{left:31px;width:205px;gap:9px}
  .feature-list--right{left:270px;width:200px;gap:6px}
  .feature-list li{position:relative;padding-left:12px}
  .feature-list li::before{content:"";position:absolute;left:0;top:3px;width:7px;height:7px;border:1px solid var(--text);border-radius:50%}
  .feature-list li::after{content:"";position:absolute;left:2.5px;top:5px;width:2px;height:3.5px;border:solid var(--text);border-width:0 1px 1px 0;transform:rotate(45deg)}
  .elevation{position:absolute;top:351px;width:200px;height:92px;border:1px solid var(--line);background:linear-gradient(180deg,#fafafa,#d9d9d9)}
  .elevation--front{left:30px}
  .elevation--rear{left:258px}

  .quality-tab{position:absolute;left:33px;top:504px;width:172px;height:18px;background:var(--tan);color:var(--peach);
    font-family:"Michroma",sans-serif;font-size:8.5px;display:flex;align-items:center;justify-content:center;letter-spacing:0.3px;z-index:2}
  .brand{position:absolute;top:537px;width:80px;display:flex;flex-direction:column;align-items:center;gap:6px}
  .brand--build{left:33px}
  .brand--residences{left:125px}
  .brand-mark{width:46px;height:46px;background:var(--tan)}
  .brand-name{font-family:"Roboto",sans-serif;font-weight:700;font-size:10.5px;line-height:12px;color:var(--white);text-align:center}
  .contact{position:absolute;right:31px;top:524px;width:230px;text-align:right}
  .contact-lead{font-size:11.8px;color:var(--white);white-space:nowrap}
  .contact-phone{margin-top:5px;height:26px;background:var(--tan);color:var(--white);font-family:"Michroma",sans-serif;font-size:18px;
    display:flex;align-items:center;justify-content:center;letter-spacing:1px}
  .contact-web{margin-top:9px;font-family:"Michroma",sans-serif;font-size:9px;line-height:18px;color:var(--white);white-space:nowrap}
</style>
</head>
<body>
  <section class="sheet sheet--front">
    <div class="hero-render" role="img" aria-label="Rendering of a modern two-storey semi-detached home with stone facade and double garage"></div>
    <h1 class="headline-band">4 UNITS AVAILABLE <strong>FOR SALE</strong></h1>
    <div class="plan-area">
      <div class="plan-section" role="img" aria-label="Building cross-section drawing"></div>
      <div class="plan-roof" role="img" aria-label="Roof plan drawing"></div>
    </div>
    <div class="quality-tab">BUILD WITH QUALITY BY</div>
    <div class="brand brand--build"><div class="brand-mark"></div><div class="brand-name">HALVOR BUILD GROUP</div></div>
    <div class="brand brand--residences"><div class="brand-mark"></div><div class="brand-name">HALVOR RESIDENCES</div></div>
    <div class="contact">
      <p class="contact-lead">For inquiries and pricing, please contact</p>
      <p class="contact-phone">905 314 6782</p>
      <p class="contact-web">www.halvorbuildgroup.ca<br>www.halvorresidencesdunmore.com</p>
    </div>
  </section>

  <section class="sheet sheet--back">
    <h2 class="features-head"><span>LUXURIOUS</span>FEATURES AND FINISHES</h2>
    <div class="features-body">
      <ul class="feature-list feature-list--left">
        <li>10 Ft ceilings on main floor</li>
        <li>9 Ft ceilings on 2nd floor</li>
        <li>9 Ft ceilings in basement</li>
        <li>12" x 24" tiles throughout home</li>
        <li>24" x 24" tiles in kitchen and ensuite</li>
        <li>9 ft high kitchen cabinets complete with crown moulding and light valences</li>
        <li>Home security rough in complete with keypads at front door, mud room and master bedroom</li>
        <li>Gas fireplace on main floor</li>
        <li>Mudroom area complete with locker and bench area</li>
        <li>Walk through pantry off kitchen complete with shelving, cabinetry, and countertop space</li>
        <li>30 LED potlights through interior of home and 5 LED potlights for exterior</li>
      </ul>
      <ul class="feature-list feature-list--right">
        <li>Large eat in kitchen island</li>
        <li>Granite and quartz countertops throughout home</li>
        <li>Engineered hardwood floor on main floor and all bedrooms</li>
        <li>4 bedrooms</li>
        <li>3.5 bathrooms</li>
        <li>2 custom tile showers</li>
        <li>2 ton Air Conditioning unit</li>
        <li>HRV unit</li>
        <li>Programmable thermostat with WIFI</li>
        <li>Finished space in basement complete with 4 piece washroom and recreation room area</li>
        <li>Large backyard</li>
        <li>Concrete driveway to be included</li>
        <li>10" thick foundation wall</li>
        <li>Poured concrete partition wall for extra sound and fire protection</li>
      </ul>
      <div class="elevation elevation--front" role="img" aria-label="Front elevation drawing"></div>
      <div class="elevation elevation--rear" role="img" aria-label="Rear elevation drawing"></div>
    </div>
    <div class="quality-tab">BUILD WITH QUALITY BY</div>
    <div class="brand brand--build"><div class="brand-mark"></div><div class="brand-name">HALVOR BUILD GROUP</div></div>
    <div class="brand brand--residences"><div class="brand-mark"></div><div class="brand-name">HALVOR RESIDENCES</div></div>
    <div class="contact">
      <p class="contact-lead">For inquiries and pricing, please contact</p>
      <p class="contact-phone">905 314 6782</p>
      <p class="contact-web">www.halvorbuildgroup.ca<br>www.halvorresidencesdunmore.com</p>
    </div>
  </section>
</body>
</html>
```